BRAVOK PRESSURE WASHING LLC

am starting a small pressure washing business in myrtle beach. I need a weebsite that will get people attention. I wanrto advertise our services . Main two : We specialize in roof cleaning , window cleaning . Other services are : residential and commercial, driveways & sidewalks, gutter cleaning, patio & deck cleaning, curb appeal, heavy equipment, mobile homes, car lots, fleets, store fronts, commercial buildings, grocery kart sanitizing, have a couple phrases saying. " Make your home shine" " Make your home look new again" I need a section showing our work in the past. Im going to send you some ,before and after pictures of our work. Also put the 100% satisfaction guaranteed ribbon somewhere on the website and give us a call for your free estiment 843 555 0176. Licensed and insured. Also need a page listing our services and a paragraph or two of the importance of that service. Maybe a section where customers can comment and give good reviews. I need it to have my logo and make it look modern and catch the eye . We founded in 2019 and use environmental amd pet friendly chemicals and top of the line pressure washing equipment. Thank you.l

```html
<!DOCTYPE html>
<html lang="en">
<head>
<meta charset="utf-8">
<title>Bravok Pressure Washing LLC</title>
<link href="https://fonts.googleapis.com/css2?family=Lato:ital,wght@0,400;0,700;0,900;1,400&display=swap" rel="stylesheet">
<style>
:root{
  --blue:#1a7fd4;
  --blue-dark:#0f5fae;
  --navy:#0b2244;
  --orange:#f6921e;
  --ink:#1d1d1d;
  --grey-bg:#efefef;
  --text:#333;
  --white:#fff;
}
*{margin:0;padding:0;box-sizing:border-box}
html,body{width:1200px;height:3644px;overflow:hidden}
body{font-family:'Lato',sans-serif;color:var(--text);background:var(--white);position:relative}
a{text-decoration:none}
.abs{position:absolute}
.photo{position:absolute;overflow:hidden}

/* header */
.site-header{position:absolute;left:0;top:0;width:1200px;height:145px;background:var(--white)}
.brand{position:absolute;left:75px;top:48px;display:flex;align-items:center;gap:10px;font-weight:900;font-size:19px;color:var(--blue-dark);line-height:1.15;width:220px}
.brand-mark{width:22px;height:22px;border-radius:50%;background:var(--orange);flex:none}
.estimate{position:absolute;right:73px;top:22px;text-align:right}
.estimate small{display:block;font-size:15px;font-weight:700;color:var(--ink);letter-spacing:.2px}
.estimate strong{display:block;font-size:27px;font-weight:900;color:var(--blue-dark);margin-top:2px}
.phone-ring{position:absolute;left:821px;top:26px;width:45px;height:45px;border:2px solid var(--blue);border-radius:50%;display:flex;align-items:center;justify-content:center}
.main-nav{position:absolute;left:428px;top:90px;width:772px;height:55px;background:var(--blue);clip-path:polygon(8px 0,100% 0,100% 100%,0 100%);display:flex;align-items:center;padding-left:31px}
.main-nav a{color:var(--white);font-size:14px;font-weight:700;margin-right:38px;letter-spacing:.2px}

/* hero */
.hero{position:absolute;left:0;top:145px;width:1200px;height:554px;background:linear-gradient(160deg,#3a5f8c 0%,#5f7a6a 30%,#9c3b2c 60%,#7a2a20 100%)}
.hero h1{position:absolute;left:0;top:178px;width:1200px;text-align:center;color:var(--white);font-size:46px;font-weight:900;line-height:54px;text-shadow:0 2px 6px rgba(0,0,0,.4)}
.btn{display:inline-flex;align-items:center;justify-content:center;border-radius:26px;color:var(--white);font-weight:700}
.hero .btn{position:absolute;left:524px;top:318px;width:152px;height:50px;background:var(--orange);font-size:15px}
.dots{position:absolute;left:562px;top:487px;display:flex;gap:11px}
.dots span{width:11px;height:11px;border-radius:50%;background:var(--white)}
.dots span:first-child{background:var(--orange)}

/* feature cards */
.feature{position:absolute;top:764px;width:512px;height:340px;border-radius:12px;overflow:hidden;display:flex;align-items:center;justify-content:center}
.feature span{position:relative;color:var(--white);font-size:40px;font-weight:900;text-shadow:0 2px 6px rgba(0,0,0,.5)}

/* welcome */
.welcome{position:absolute;left:0;top:1178px;width:1200px;height:460px;background:var(--navy);overflow:hidden}
.welcome h2{position:absolute;left:76px;top:58px;font-size:36px;font-weight:900;line-height:39px;color:var(--white)}
.welcome h2 em{font-style:normal;color:var(--orange);display:block}
.welcome p{position:absolute;left:75px;top:148px;width:515px;font-size:13.5px;line-height:24px;color:#e6ebf3}
.welcome .btn{position:absolute;left:75px;top:344px;width:151px;height:50px;background:var(--blue);font-size:15px}

/* services */
.section-title{position:absolute;left:0;width:1200px;text-align:center;font-size:35px;font-weight:900;color:var(--ink)}
.tile{position:absolute;width:331px;height:228px;border-radius:8px;overflow:hidden;display:flex;align-items:center;justify-content:center;text-align:center}
.tile span{position:relative;color:var(--white);font-size:23px;font-weight:900;line-height:31px;text-shadow:0 2px 5px rgba(0,0,0,.55)}
.tile.cta{background:var(--orange);flex-direction:column;gap:14px}
.tile.cta span{text-shadow:none;font-size:24px}

/* work */
.work{position:absolute;left:0;top:2306px;width:1200px;height:546px;background:var(--grey-bg)}
.ba{position:absolute;top:130px;width:331px;height:254px;border-radius:8px;overflow:hidden}
.ba .half{position:absolute;top:0;height:100%}
.ba .divider{position:absolute;left:163px;top:0;width:4px;height:100%;background:#f2c500}
.ba label{position:absolute;bottom:14px;color:var(--white);font-size:11px;font-weight:900}
.work .btn{position:absolute;left:499px;top:439px;width:203px;height:50px;background:var(--blue);font-size:15px}

/* reviews */
.reviews-title{position:absolute;left:85px;top:2905px;font-size:36px;font-weight:900;color:var(--ink)}
.review{position:absolute;top:2982px;width:328px;height:112px;background:var(--navy);padding:14px 20px 0 24px}
.review::after{content:"";position:absolute;left:62px;bottom:-22px;border-right:30px solid transparent;border-top:22px solid var(--navy)}
.review p{font-style:italic;font-size:14px;line-height:24px;color:var(--white)}
.review .q{position:absolute;left:10px;top:4px;font-size:48px;font-weight:900;color:var(--blue);line-height:1}
.author{position:absolute;top:3162px;display:flex;align-items:center;gap:15px}
.avatar{width:74px;height:74px;border-radius:50%;background:linear-gradient(135deg,#d9d4cc,#8c8680)}
.author b{display:block;color:var(--blue);font-size:16px;font-weight:700}
.author small{display:block;font-size:12px;color:#444;margin-top:4px}
.guarantee{position:absolute;left:794px;top:2917px;width:332px;height:319px;border-radius:8px;background:linear-gradient(180deg,#0f6fc6 0%,#0b3f82 60%,#0b2e62 100%);text-align:center}
.guarantee .seal{position:absolute;left:96px;top:14px;width:140px;height:176px;border-radius:8px;background:linear-gradient(180deg,#d9ad3a 0%,#c9973a 60%,#b3121f 100%);opacity:.9}
.guarantee h3{position:absolute;left:0;top:216px;width:100%;color:var(--white);font-size:19px;font-weight:900;line-height:24px}
.guarantee strong{position:absolute;left:0;top:264px;width:100%;color:var(--orange);font-size:34px;font-weight:900}

/* footer */
.site-footer{position:absolute;left:0;top:3297px;width:1200px;height:347px;background:var(--grey-bg)}
.site-footer .brand{left:75px;top:70px;width:190px;font-size:18px}
.copyright{position:absolute;left:75px;top:195px;font-size:11px;line-height:16px;color:#333}
.socials{position:absolute;left:77px;top:250px;display:flex;gap:15px}
.socials span{width:17px;height:17px;border-radius:50%;background:var(--blue)}
.foot-col{position:absolute;top:54px}
.foot-col h4{font-size:13px;font-weight:900;color:var(--ink);margin-bottom:11px}
.foot-col ul{list-style:none}
.foot-col li{font-size:13.5px;line-height:29px;color:#333}
.contact-list{list-style:none}
.contact-list li{display:flex;gap:12px;font-size:13px;line-height:20px;margin-bottom:11px;color:#333}
.contact-list svg{flex:none;margin-top:2px}
.contact-name{font-size:14px;font-weight:700;color:var(--blue);margin-bottom:10px}
</style>
</head>
<body>

<header class="site-header">
  <div class="brand"><span class="brand-mark"></span>BRAVOK PRESSURE WASHING LLC</div>
  <div class="phone-ring">
    <svg width="20" height="20" viewBox="0 0 24 24"><path d="M6.6 10.8c1.4 2.8 3.8 5.1 6.6 6.6l2.2-2.2c.3-.3.7-.4 1-.2 1.1.4 2.3.6 3.6.6.6 0 1 .4 1 1V20c0 .6-.4 1-1 1C10.6 21 3 13.4 3 4c0-.6.4-1 1-1h3.5c.6 0 1 .4 1 1 0 1.3.2 2.5.6 3.6.1.3 0 .7-.2 1z" fill="#f6921e"/></svg>
  </div>
  <div class="estimate"><small>CALL FOR YOUR FREE ESTIMATE</small><strong>843 555 0176</strong></div>
  <nav class="main-nav">
    <a href="#">HOME</a><a href="#">ABOUT US</a><a href="#">SERVICES</a><a href="#">WORK GALLERY</a><a href="#">TESTIMONIALS</a><a href="#">CONTACT US</a>
  </nav>
</header>

<section class="hero" role="img" aria-label="Worker pressure washing a red tiled roof beside a brick chimney">
  <h1>MAKE YOUR HOME SHINE<br>MAKE YOUR HOME LOOK NEW AGAIN</h1>
  <a class="btn" href="#">READ MORE</a>
  <div class="dots"><span></span><span></span><span></span><span></span></div>
</section>

<a class="feature" href="#" style="left:75px">
  <div class="photo" style="inset:0;background:linear-gradient(150deg,#2a6a9e,#1b4f86 50%,#0f3a70)" role="img" aria-label="Roof being pressure cleaned"></div>
  <span>ROOF CLEANING</span>
</a>
<a class="feature" href="#" style="left:615px">
  <div class="photo" style="inset:0;background:linear-gradient(150deg,#3a8fd6,#1a6ab8 55%,#0e4f98)" role="img" aria-label="Window being pressure cleaned"></div>
  <span>WINDOW CLEANING</span>
</a>

<section class="welcome">
  <h2>WELCOME TO<em>BRAVOK PRESSURE WASHING</em></h2>
  <p>Donec quis augue quis magna condimentum lobortis. Quisque imperdiet ipsum vel magna viverra rutrum. Cras viverra molestie urna, vitae vestibulum turpis varius id. Vestibulum mollis, arcu iaculis bibendum varius, velit sapien blandit metus, ac posuere lorem nulla ac dolor. Maecenas urna elit, tincidunt in dapibus nec, vehicula eu du uis lacinia. fringilla massa. Cum sociis natoque penatibus et magnis dis parturient montes, nascetur ridiculus mus. Integer bibendum sagittis ligula, non faucibus nulla volutpat vitae.</p>
  <a class="btn" href="#">READ MORE</a>
  <svg class="abs" style="left:600px;top:0" width="600" height="460" viewBox="0 0 600 460">
    <path d="M110 0 C20 90 -10 330 60 460 L600 460 L600 0 Z" fill="#f6921e"/>
  </svg>
  <div class="photo" style="left:620px;top:0;width:580px;height:460px;clip-path:path('M104 0 C18 92 -6 330 62 460 L580 460 L580 0 Z');background:linear-gradient(160deg,#a9a39a,#cfcac2 45%,#8d8a86)" role="img" aria-label="Worker in blue boots pressure washing a paved walkway"></div>
</section>

<h2 class="section-title" style="top:1680px">OUR SERVICES</h2>
<div class="tile" style="left:75px;top:1758px"><div class="photo" style="inset:0;background:linear-gradient(135deg,#4a6f8e,#7c8e9a)" role="img" aria-label="Worker washing a house wall"></div><span>RESIDENTIAL<br>&amp; COMMERCIAL</span></div>
<div class="tile" style="left:436px;top:1758px"><div class="photo" style="inset:0;background:linear-gradient(135deg,#6b4b3a,#9a9592)" role="img" aria-label="Storefront sidewalk"></div><span>DRIVEWAYS<br>&amp; SIDEWALKS</span></div>
<div class="tile" style="left:796px;top:1758px"><div class="photo" style="inset:0;background:linear-gradient(135deg,#7a8a4a,#2b3f6a)" role="img" aria-label="Hands clearing leaves from a gutter"></div><span>GUTTER CLEANING</span></div>
<div class="tile" style="left:75px;top:2010px"><div class="photo" style="inset:0;background:linear-gradient(135deg,#5a5448,#3a3a3c)" role="img" aria-label="Wooden deck being washed"></div><span>PATIO &amp; DECK<br>CLEANING</span></div>
<div class="tile" style="left:436px;top:2010px"><div class="photo" style="inset:0;background:linear-gradient(180deg,#2a3a5e,#6a6e78)" role="img" aria-label="Clean house front at dusk"></div><span>CURB APPEAL</span></div>
<a class="tile cta" href="#" style="left:796px;top:2010px"><span>VIEW ALL SERVICES</span>
  <svg width="46" height="22" viewBox="0 0 46 22"><path d="M2 11h38M30 3l9 8-9 8" stroke="#fff" stroke-width="4" fill="none" stroke-linecap="round"/></svg></a>

<section class="work">
  <h2 class="section-title" style="top:48px">OUR WORK</h2>
  <svg class="abs" style="left:44px;top:245px" width="16" height="28" viewBox="0 0 16 28"><path d="M14 2 2 14l12 12" stroke="#333" stroke-width="2" fill="none"/></svg>
  <svg class="abs" style="left:1140px;top:245px" width="16" height="28" viewBox="0 0 16 28"><path d="M2 2l12 12L2 26" stroke="#333" stroke-width="2" fill="none"/></svg>
  <div class="ba" style="left:75px" role="img" aria-label="House roof before and after cleaning">
    <div class="half" style="left:0;width:165px;background:linear-gradient(180deg,#5a6a5a,#3c3c3a)"></div>
    <div class="half" style="left:165px;width:166px;background:linear-gradient(180deg,#6e8a6a,#5a4a3e)"></div>
    <div class="divider"></div><label style="left:15px">BEFORE</label><label style="left:181px">AFTER</label>
  </div>
  <div class="ba" style="left:436px" role="img" aria-label="Driveway before and after cleaning">
    <div class="half" style="left:0;width:165px;background:linear-gradient(180deg,#6a7a62,#77756e)"></div>
    <div class="half" style="left:165px;width:166px;background:linear-gradient(180deg,#4e6448,#b4b0a8)"></div>
    <div class="divider"></div><label style="left:19px">BEFORE</label><label style="left:185px">AFTER</label>
  </div>
  <div class="ba" style="left:796px" role="img" aria-label="Parking pad before and after cleaning">
    <div class="half" style="left:0;width:165px;background:linear-gradient(180deg,#5c6e78,#3e4a4e)"></div>
    <div class="half" style="left:165px;width:166px;background:linear-gradient(180deg,#6e7e84,#9a9690)"></div>
    <div class="divider"></div><label style="left:19px">BEFORE</label><label style="left:185px">AFTER</label>
  </div>
  <a class="btn" href="#">VIEW ALL WORK</a>
</section>

<h2 class="reviews-title">CUSTOMER REVIEWS</h2>
<div class="review" style="left:86px"><span class="q">&ldquo;</span><p>Aenean a nibh eget turpis vehicula tempus ac sed massa. Vestibulum dolor nulla, ultrices ac tincidunt sed, laoreet non est. Suspendisse lobortis turpis in odio blandit ac interdum..</p></div>
<div class="review" style="left:434px"><span class="q">&ldquo;</span><p>Aenean a nibh eget turpis vehicula tempus ac sed massa. Vestibulum dolor nulla, ultrices ac tincidunt sed, laoreet non est. Suspendisse lobortis turpis in odio blandit ac interdum..</p></div>
<div class="author" style="left:87px"><div class="avatar" role="img" aria-label="Customer portrait"></div><div><b>Carter</b><small>Conway</small></div></div>
<div class="author" style="left:434px"><div class="avatar" role="img" aria-label="Customer portrait"></div><div><b>Carter</b><small>Conway</small></div></div>

<aside class="guarantee">
  <div class="seal" role="img" aria-label="100% satisfaction guaranteed ribbon seal"></div>
  <h3>GIVE US A CALL FOR YOUR<br>FREE ESTIMATE</h3>
  <strong>843 555 0176</strong>
</aside>

<footer class="site-footer">
  <div class="brand"><span class="brand-mark"></span>BRAVOK PRESSURE WASHING LLC</div>
  <div class="copyright">Copyright © 2020. Bravok Pressure Washing LLC<br>All Right Reserved</div>
  <div class="socials"><span></span><span></span><span></span><span></span><span></span><span></span></div>
  <div class="foot-col" style="left:328px"><h4>SITE MAP</h4><ul><li>Home</li><li>About Us</li><li>Services</li><li>Work Gallery</li><li>Testimonials</li><li>Contact Us</li></ul></div>
  <div class="foot-col" style="left:505px"><h4>SERVICES</h4><ul><li>Residential &amp; Commercial</li><li>Driveways &amp; Sidewalks</li><li>Gutter Cleaning</li><li>Patio &amp; Deck Cleaning</li><li>Curb Appeal</li><li>Heavy Equipment</li></ul></div>
  <div class="foot-col" style="left:696px"><h4>&nbsp;</h4><ul><li>Mobile Homes</li><li>Car Lots</li><li>Fleets</li><li>Store Fronts</li><li>Commercial Buildings</li><li>Grocery Cart Sanitizing</li></ul></div>
  <div class="foot-col" style="left:913px"><h4>CONTACT US</h4>
    <div class="contact-name">Bravok Pressure Washing</div>
    <ul class="contact-list">
      <li><svg width="15" height="15" viewBox="0 0 24 24"><path d="M12 2a7 7 0 0 0-7 7c0 5 7 13 7 13s7-8 7-13a7 7 0 0 0-7-7zm0 9.5A2.5 2.5 0 1 1 12 6a2.5 2.5 0 0 1 0 5.5z" fill="#f6921e"/></svg><span>Cum sociis natoque<br>penatibus</span></li>
      <li><svg width="15" height="15" viewBox="0 0 24 24"><path d="M6.6 10.8c1.4 2.8 3.8 5.1 6.6 6.6l2.2-2.2c.3-.3.7-.4 1-.2 1.1.4 2.3.6 3.6.6.6 0 1 .4 1 1V20c0 .6-.4 1-1 1C10.6 21 3 13.4 3 4c0-.6.4-1 1-1h3.5c.6 0 1 .4 1 1 0 1.3.2 2.5.6 3.6.1.3 0 .7-.2 1z" fill="#f6921e"/></svg><span>843 555 0176</span></li>
      <li><svg width="15" height="15" viewBox="0 0 24 24"><rect x="2" y="5" width="20" height="14" rx="2" fill="#f6921e"/><path d="M3 6l9 7 9-7" stroke="#fff" stroke-width="1.6" fill="none"/></svg><span>info@bravokwash.com</span></li>
    </ul>
  </div>
</footer>

</body>
</html>
```